Fotógrafo necesita portada completa para un libro de negocios enfocado a fotografía

Necesito la portada, contraportada y lomo de un libro de tapa blanda que venderé en Vendalia llamado “Las claves para prosperar con la cámara”. Adjunto medidas requeridas por Vendalia.

“Las claves para prosperar con la cámara” es un libro de negocios orientado a fotógrafos, no un libro de fotografía en sí mismo. Detallo las necesidades a continuación:

- Descripción general: Necesito que el diseño sea llamativo, pero lo suficientemente sencillo, moderno y atractivo como para que el cliente perciba en el diseño que el interior contiene un gran valor. No quiero elementos recargados ni diseños muy complicados de entender. Para más inspiración, ver las portadas de libros como "Las mañas del patrón", "La mente del ahorro", "rutinas mínimas", siguiendo el estilo de mi marca personal: www.ruperbelo.es
- Portada: La portada debe expresar sensaciones de emoción y libertad (al emprender un negocio fotográfico de la forma que transmito en el interior del libro), pero también de misterio (debido a esos “secretos” para vivir del negocio de la fotografía)
- Contraportada: dividida en dos secciones: Una para la breve descripción del libro y otra para la descripción de la biografía del autor con foto.

Por último, necesito el diseño editable en .PSD con los textos provisionales “lorem ipsum”, ya que todavía no tengo los textos definitivos y seré yo quien los integre, así que aprovecharé esos campos de texto, con la fuente, tamaño y color para hacerlo.

Target Market(s)

Photographers

Industry/Entity Type

Photography, economy, marketing

Font styles to use
Serif
Sans Serif

Requirements
Must have
• Title: Las claves para prosperar con la cámara (Capital or not. Depending on design), Subtitle: El manual completo para trabajar de retratista sin perder la cabeza jamás. Author: Ruper Belo
Should not have
• pictures, photos, ¿gradients?

```html
<!DOCTYPE html>
<html lang="es">
<head>
<meta charset="utf-8">
<title>Las claves para prosperar con la cámara — Ruper Belo</title>
<link rel="stylesheet" href="https://fonts.googleapis.com/css2?family=Playfair+Display:wght@900&family=Playfair+Display+SC:wght@700&family=Josefin+Sans:wght@600&family=Cinzel:wght@400&display=swap">
<style>
  :root {
    --backdrop: #d4d5d7;
    --paper: #ffffff;
    --ink: #141414;
    --gold: #b8892e;
    --gold-soft: #dcc28c;
    --photo-tone: #e9ecdf;
  }
  * { margin: 0; padding: 0; box-sizing: border-box; }
  html, body {
    width: 850px; height: 1200px; overflow: hidden;
    background: var(--backdrop);
  }
  .cover {
    position: absolute; left: 35px; top: 15px;
    width: 780px; height: 1170px;
    background: var(--paper);
    overflow: hidden;
  }
  .title-block {
    position: absolute; left: 0; top: 0; width: 100%; height: 460px;
    transform: rotate(-2.5deg);
    transform-origin: 50% 250px;
  }
  .title-block h1 { font-weight: normal; }
  .rule {
    position: absolute; height: 6px;
    border-top: 2px solid var(--gold);
    border-bottom: 1px solid var(--gold);
  }
  .rule::after {
    content: ""; position: absolute; top: -4px; width: 8px; height: 8px;
    border-radius: 50%; background: var(--gold);
  }
  .rule.left::after { left: -14px; }
  .rule.right::after { right: -14px; }
  .title-small, .title-mid, .title-big {
    position: absolute; left: 0; width: 100%; text-align: center;
    line-height: 1; white-space: nowrap;
  }
  .title-small, .title-mid {
    font-family: "Playfair Display SC", serif; font-weight: 700;
    color: var(--gold);
  }
  .title-small { top: 48px; font-size: 50px; }
  .title-mid { top: 232px; font-size: 40px; }
  .title-big {
    font-family: "Playfair Display", serif; font-weight: 900;
    color: var(--ink); font-size: 145px; letter-spacing: 1px;
    text-shadow: 6px 6px 0 var(--gold-soft);
  }
  .title-big.first { top: 86px; }
  .title-big.second { top: 282px; }
  .subtitle {
    position: absolute; left: 0; top: 448px; width: 100%;
    font-family: "Josefin Sans", sans-serif; font-weight: 600;
    font-size: 20px; letter-spacing: 1.5px; line-height: 1.35;
    color: var(--ink); text-align: center; text-transform: uppercase;
    white-space: nowrap;
    transform: rotate(-3deg);
  }
  .cover-photo {
    position: absolute; left: 120px; top: 515px;
    width: 560px; height: 470px;
    background: var(--photo-tone);
  }
  .author {
    position: absolute; left: 0; top: 1058px; width: 100%; text-align: center;
  }
  .author-name {
    font-family: "Cinzel", serif; font-size: 40px; color: var(--ink);
    letter-spacing: 1px; line-height: 1;
  }
  .author-rule {
    width: 300px; height: 5px; margin: 8px auto;
    border-top: 1px solid var(--gold); border-bottom: 1px solid var(--gold);
  }
</style>
</head>
<body>
  <main class="cover">
    <header class="title-block">
      <span class="rule left" style="left:78px; top:78px; width:240px;"></span>
      <span class="rule right" style="left:462px; top:72px; width:240px;"></span>
      <span class="rule left" style="left:70px; top:258px; width:55px;"></span>
      <span class="rule right" style="left:655px; top:250px; width:55px;"></span>
      <h1>
        <span class="title-small">Las</span>
        <span class="title-big first">CLAVES</span>
        <span class="title-mid">Para prosperar con la</span>
        <span class="title-big second">CÁMARA</span>
      </h1>
    </header>

    <p class="subtitle">El manual completo para trabajar de retratista<br>sin perder la cabeza jamás.</p>

    <div class="cover-photo" role="img" aria-label="Fotografía de una cámara réflex hecha con billetes doblados en papiroflexia"></div>

    <footer class="author">
      <div class="author-rule"></div>
      <p class="author-name">Ruper Belo</p>
      <div class="author-rule"></div>
    </footer>
  </main>
</body>
</html>
```